We need a fresh, new church business card!!

We need a church business card with basic info to hand out as invites. We are looking for something clean that communicates our basic information clearly.

We are open to square or rectangle card sizes.

General Public

Religious

The attached logo is the only one that I have available. We'd like to see options with with text of the logo lighter and on a dark background as well as options with white/light backgrounds.

Also, we'd like to see option with rounded corners.

• Address - 2718 Maple Row, Rockford, IL 61142
• Website - brookvane.example
• Phone - 815-555-0163
• Service times -
• Sunday - 10am Sunday School
• - 11am Family Worship
• - 6pm Night of Prayer
• Wednesday - 7:30pm Adult Bible Study
• Classes for all ages

```html
<!DOCTYPE html>
<html lang="en">
<head>
<meta charset="utf-8">
<title>Brookvane Pentecostal Church – Business Card</title>
<link href="https://fonts.googleapis.com/css2?family=Open+Sans:wght@400;600;700&display=swap" rel="stylesheet">
<style>
  :root {
    --backdrop: #3a3a3c;
    --card: #050505;
    --teal: #5b9fb0;
    --silver: #8f8f93;
    --white: #f4f4f4;
    --rule: #4a4a4a;
  }
  * { box-sizing: border-box; margin: 0; padding: 0; }
  html, body { width: 1200px; height: 900px; overflow: hidden; }
  body {
    background: var(--backdrop);
    font-family: "Open Sans", Arial, sans-serif;
    color: var(--white);
    position: relative;
  }
  .card {
    position: absolute;
    left: 260px;
    width: 680px;
    height: 390px;
    background: var(--card);
    border-radius: 28px;
    box-shadow: 0 14px 30px rgba(0,0,0,.45);
  }
  .card--front { top: 45px; }
  .card--back { top: 465px; }

  /* Front */
  .brand {
    position: absolute;
    left: 120px;
    top: 130px;
    display: flex;
    align-items: center;
    gap: 22px;
  }
  .brand__dot {
    width: 78px; height: 78px;
    border-radius: 50%;
    background: var(--teal);
  }
  .brand__name {
    color: var(--silver);
    font-weight: 400;
    font-size: 30px;
    letter-spacing: 2px;
    line-height: 1.15;
    text-transform: uppercase;
  }
  .schedule { position: absolute; font-size: 17px; line-height: 1.22; }
  .schedule__label {
    color: var(--teal);
    font-weight: 600;
    text-transform: uppercase;
    letter-spacing: .5px;
  }
  .schedule--sunday { left: 44px; bottom: 40px; }
  .schedule--wednesday { right: 40px; top: 36px; text-align: right; }

  /* Back */
  .mark {
    position: absolute;
    left: 70px;
    top: 115px;
    display: flex;
    flex-direction: column;
    align-items: center;
    gap: 16px;
  }
  .mark__dot {
    width: 120px; height: 120px;
    border-radius: 50%;
    background: var(--teal);
  }
  .mark__name {
    color: var(--teal);
    font-size: 24px;
    font-weight: 400;
    letter-spacing: 3px;
    text-transform: uppercase;
  }
  .divider {
    position: absolute;
    left: 330px;
    top: 90px;
    width: 1px;
    height: 210px;
    background: var(--rule);
  }
  .contact {
    position: absolute;
    left: 360px;
    top: 92px;
    font-size: 16px;
    line-height: 1.3;
  }
  .contact__name { font-size: 26px; font-weight: 700; letter-spacing: .5px; line-height: 1.1; }
  .contact__role {
    color: var(--teal);
    font-size: 15px;
    font-weight: 600;
    text-transform: uppercase;
    margin-bottom: 14px;
  }
  .contact__address { margin-bottom: 10px; }
  .contact__line { display: flex; align-items: center; gap: 8px; }
  .contact__line svg { width: 13px; height: 13px; flex: none; }
</style>
</head>
<body>

<section class="card card--front">
  <div class="brand">
    <div class="brand__dot"></div>
    <div class="brand__name">Brookvane<br>Pentecostal Church</div>
  </div>

  <div class="schedule schedule--wednesday">
    <div class="schedule__label">Wednesday:</div>
    <div>7:30pm Adult Bible Study</div>
    <div>Classes for all ages</div>
  </div>

  <div class="schedule schedule--sunday">
    <div class="schedule__label">Service Times:</div>
    <div>Sunday - 10am Sunday School</div>
    <div>11am Family Worship</div>
    <div>6pm Night of Prayer</div>
  </div>
</section>

<section class="card card--back">
  <div class="mark">
    <div class="mark__dot"></div>
    <div class="mark__name">Brookvane</div>
  </div>

  <div class="divider"></div>

  <div class="contact">
    <div class="contact__name">DANA REYES</div>
    <div class="contact__role">Director</div>
    <div class="contact__address">2718 Maple Row,<br>Rockford, IL 61142</div>
    <div class="contact__line">
      <svg viewBox="0 0 16 16" aria-hidden="true"><path fill="var(--teal)" d="M3.6 1.2l2.3 2.9-1.3 1.6c.9 2 2.6 3.7 4.6 4.6l1.6-1.3 2.9 2.3-1.2 2.1C7 13.2 2.8 9 2.4 3.2z"/></svg>
      <span>815-555-0163</span>
    </div>
    <div class="contact__line">
      <svg viewBox="0 0 16 16" aria-hidden="true"><circle cx="8" cy="8" r="6.5" fill="none" stroke="var(--teal)" stroke-width="1.6"/><path d="M1.5 8h13M8 1.5c-3 3.5-3 9.5 0 13M8 1.5c3 3.5 3 9.5 0 13" fill="none" stroke="var(--teal)" stroke-width="1.2"/></svg>
      <span>www.brookvane.example</span>
    </div>
  </div>
</section>

</body>
</html>
```